Design for online reviews widget

Attached is a wireframe of a widget we need designing to display reviews on websites from multiple sources. We need this provided at 3 different sizes including full screen, contained (like the wireframe) and mobile.
You have completely free rein on the styling.
The only elements that should remain untouched are the blue stars (https://www.filquarry.net/s/8vtmwp2291zq4h/kv%20stars.ai?dl=0) and powered by logo at the bottom.
Ignore the menu at the top of the wireframe, this is just from the website the widget will be placed on.
Businesses

```html
<!DOCTYPE html>
<html lang="en">
<head>
<meta charset="utf-8">
<title>Reviews Widget – Responsive Sizes</title>
<link href="https://fonts.googleapis.com/css2?family=Montserrat:wght@300;400;500;600;700&display=swap" rel="stylesheet">
<style>
  :root{
    --canvas:#ffffff;
    --panel:#f0f0f0;
    --card:#ffffff;
    --ink:#1c1c1c;
    --muted:#6f6f6f;
    --label:#2a2a2a;
    --brand-blue:#3cb9e8;
    --verified:#5aa61e;
    --border:#dcdcdc;
    --chip-rel:#eaf0f8;
    --chip-cou:#eef6ea;
    --chip-tid:#fbecec;
    --chip-wor:#fdf1e4;
  }
  *{box-sizing:border-box;margin:0;padding:0}
  html,body{width:1120px;height:1200px;overflow:hidden}
  body{background:var(--canvas);font-family:"Montserrat",sans-serif;color:var(--ink);position:relative}

  .size-label{position:absolute;font-weight:300;font-size:22px;color:var(--label);letter-spacing:.5px}

  .widget{position:absolute;background:var(--panel);box-shadow:0 10px 40px rgba(0,0,0,.12)}

  .rating-stars{display:flex;gap:1px}
  .rating-stars svg{width:17px;height:17px;display:block}
  .score-text{font-size:5.6px;margin-top:4px;color:var(--ink)}
  .filter{position:absolute;width:114px;height:16px;background:#fff;border:1px solid var(--border);
    font-size:5.4px;color:#8a8a8a;display:flex;align-items:center;justify-content:space-between;padding:0 7px}
  .filter svg{width:6px;height:4px}

  .review{position:absolute;background:var(--card);display:flex;align-items:flex-start}
  .review.is-active{box-shadow:0 2px 8px rgba(80,130,200,.18)}
  .source{width:88px;height:100%;display:flex;align-items:center;justify-content:center;flex-shrink:0}
  .source-name{font-size:10px;font-weight:600;color:var(--ink);display:flex;align-items:center;gap:3px}
  .source-name i{width:6px;height:6px;border-radius:50%;background:var(--ink);display:inline-block}
  .review-body{padding-top:14px;padding-right:24px}
  .review-title{font-size:8.4px;font-weight:600;line-height:10px}
  .scores{display:flex;margin-top:3px;font-size:5.5px}
  .scores span{padding:1px 3px;line-height:7px}
  .scores b{font-weight:600}
  .scores .rel{background:var(--chip-rel)}
  .scores .cou{background:var(--chip-cou)}
  .scores .tid{background:var(--chip-tid)}
  .scores .wor{background:var(--chip-wor)}
  .review-text{font-size:5.5px;line-height:7.2px;color:var(--muted);margin-top:6px}
  .verified{font-size:5px;color:var(--verified);margin-top:13px;margin-left:-1px}

  .load-more{position:absolute;width:118px;height:25px;background:var(--brand-blue);color:#fff;border-radius:3px;
    font-size:8px;font-weight:600;display:flex;align-items:center;justify-content:center}
  .powered{position:absolute;width:88px;display:flex;align-items:center;gap:4px}
  .powered-mark{width:14px;height:14px;border-radius:50%;background:var(--brand-blue);flex-shrink:0}
  .powered-text small{display:block;font-size:6px;color:var(--ink);margin-bottom:1px}
  .powered-text strong{display:block;font-size:10px;font-weight:700;color:var(--ink);line-height:11px}

  .widget-mobile .header{display:flex;flex-direction:column;align-items:center;padding-top:17px}
  .widget-mobile .review{flex-direction:column;align-items:center;text-align:center;padding:10px 7px 0;width:147px;height:175px;left:12px}
  .widget-mobile .source{width:auto;height:22px}
  .widget-mobile .review-body{padding:0}
  .widget-mobile .review-title{margin-top:4px;font-size:8px}
  .widget-mobile .scores{display:grid;grid-template-columns:auto auto;width:max-content;margin:6px auto 0}
  .widget-mobile .scores span{text-align:left;padding:0 3px;line-height:7px}
  .widget-mobile .review-text{margin-top:7px}
  .widget-mobile .verified{margin-top:10px;line-height:6px;margin-left:0}
</style>
</head>
<body>

<svg width="0" height="0" style="position:absolute">
  <defs>
    <symbol id="star-badge" viewBox="0 0 20 20">
      <circle cx="10" cy="10" r="10" fill="#3cb9e8"/>
      <circle cx="10" cy="10" r="8" fill="none" stroke="#fff" stroke-width="1"/>
      <path d="M10 4.2l1.75 3.6 3.95.55-2.87 2.77.7 3.93L10 13.2l-3.53 1.85.7-3.93L4.3 8.35l3.95-.55z" fill="#fff"/>
    </symbol>
    <symbol id="chevron" viewBox="0 0 6 4"><path d="M.5.5L3 3 5.5.5" fill="none" stroke="#555" stroke-width=".8"/></symbol>
  </defs>
</svg>

<!-- ============ FULL SCREEN ============ -->
<div class="size-label" style="left:67px;top:24px">1920</div>
<section class="widget widget-wide" style="left:67px;top:59px;width:762px;height:518px">
  <div style="position:absolute;left:18px;top:18px">
    <div class="rating-stars">
      <svg><use href="#star-badge"/></svg><svg><use href="#star-badge"/></svg><svg><use href="#star-badge"/></svg><svg><use href="#star-badge"/></svg><svg><use href="#star-badge"/></svg>
    </div>
    <p class="score-text">Combined Review Score of: 4.3 out of 5</p>
  </div>
  <div class="filter" style="left:631px;top:29px">Filter Results<svg><use href="#chevron"/></svg></div>

  <article class="review is-active" style="left:18px;top:57px;width:727px;height:85px">
    <div class="source"><span class="source-name"><i></i>Fixmark</span></div>
    <div class="review-body">
      <h3 class="review-title">Front door with windows each side and side windows</h3>
      <div class="scores"><span class="rel"><b>Reliability:</b> 9.38</span><span class="cou"><b>Courtesy:</b> 10</span><span class="tid"><b>Tidiness:</b> 9.84</span><span class="wor"><b>Workmanship:</b> 10</span></div>
      <p class="review-text">For the city, the spring trade fair is what the summer games were to the coast, just that the travel situation is not a concern in the region. The event which has been delayed by a year due to the weather, is seeing locals complain about the long wait for cabs but is also seen to be a major boost for tourism and a boost for the economy.</p>
      <p class="verified">Verified 28th September 2021 &nbsp;|&nbsp; Located in Brentwood</p>
    </div>
  </article>
  <article class="review" style="left:18px;top:152px;width:727px;height:85px">
    <div class="source"><span class="source-name"><i></i>Searchly</span></div>
    <div class="review-body">
      <h3 class="review-title">Positive Professionalism, Quality &amp; Value</h3>
      <div class="scores"><span class="rel"><b>Reliability:</b> 9.38</span><span class="cou"><b>Courtesy:</b> 10</span><span class="tid"><b>Tidiness:</b> 9.84</span><span class="wor"><b>Workmanship:</b> 10</span></div>
      <p class="review-text">For the city, the spring trade fair is what the summer games were to the coast, just that the travel situation is not a concern in the region. The event which has been delayed by a year due to the weather, is seeing locals complain about the long wait for cabs but is also seen to be a major boost for tourism and a boost for the economy.</p>
      <p class="verified">Verified 28th September 2021 &nbsp;|&nbsp; Located in Brentwood</p>
    </div>
  </article>
  <article class="review" style="left:18px;top:247px;width:727px;height:85px">
    <div class="source"><span class="source-name"><i></i>Hollr</span></div>
    <div class="review-body">
      <h3 class="review-title">Brilliant all round professional, friendly service</h3>
      <div class="scores"><span class="rel"><b>Reliability:</b> 9.38</span><span class="cou"><b>Courtesy:</b> 10</span><span class="tid"><b>Tidiness:</b> 9.84</span><span class="wor"><b>Workmanship:</b> 10</span></div>
      <p class="review-text">For the city, the spring trade fair is what the summer games were to the coast, just that the travel situation is not a concern in the region. The event which has been delayed by a year due to the weather, is seeing locals complain about the long wait for cabs but is also seen to be a major boost for tourism and a boost for the economy.</p>
      <p class="verified">Verified 28th September 2021 &nbsp;|&nbsp; Located in Brentwood</p>
    </div>
  </article>
  <article class="review" style="left:18px;top:342px;width:727px;height:85px">
    <div class="source"><span class="source-name"><i></i>Vouchly</span></div>
    <div class="review-body">
      <h3 class="review-title">Best all round professional service</h3>
      <div class="scores"><span class="rel"><b>Reliability:</b> 9.38</span><span class="cou"><b>Courtesy:</b> 10</span><span class="tid"><b>Tidiness:</b> 9.84</span><span class="wor"><b>Workmanship:</b> 10</span></div>
      <p class="review-text">For the city, the spring trade fair is what the summer games were to the coast, just that the travel situation is not a concern in the region. The event which has been delayed by a year due to the weather, is seeing locals complain about the long wait for cabs but is also seen to be a major boost for tourism and a boost for the economy.</p>
      <p class="verified">Verified 28th September 2021 &nbsp;|&nbsp; Located in Brentwood</p>
    </div>
  </article>

  <div class="load-more" style="left:322px;top:459px">Load More</div>
  <div class="powered" style="left:658px;top:457px"><span class="powered-mark"></span><div class="powered-text"><small>Powered by</small><strong>ReviewHive</strong></div></div>
</section>

<!-- ============ CONTAINED ============ -->
<div class="size-label" style="left:67px;top:613px">1280</div>
<section class="widget widget-contained" style="left:67px;top:643px;width:509px;height:514px">
  <div style="position:absolute;left:18px;top:18px">
    <div class="rating-stars">
      <svg><use href="#star-badge"/></svg><svg><use href="#star-badge"/></svg><svg><use href="#star-badge"/></svg><svg><use href="#star-badge"/></svg><svg><use href="#star-badge"/></svg>
    </div>
    <p class="score-text">Combined Review Score of: 4.3 out of 5</p>
  </div>
  <div class="filter" style="left:377px;top:29px">Filter Results<svg><use href="#chevron"/></svg></div>

  <article class="review is-active" style="left:18px;top:57px;width:473px;height:85px">
    <div class="source"><span class="source-name"><i></i>Fixmark</span></div>
    <div class="review-body">
      <h3 class="review-title">Front door with windows each side and side windows</h3>
      <div class="scores"><span class="rel"><b>Reliability:</b> 9.38</span><span class="cou"><b>Courtesy:</b> 10</span><span class="tid"><b>Tidiness:</b> 9.84</span><span class="wor"><b>Workmanship:</b> 10</span></div>
      <p class="review-text">For the city, the spring trade fair is what the summer games were to the coast, just that the travel situation is not a concern in the region. The event which has been delayed by a year due to the weather, is seeing locals complain about the long wait for cabs but is also seen to be a major boost for tourism and a boost for the economy.</p>
      <p class="verified" style="margin-top:6px">Verified 28th September 2021 &nbsp;|&nbsp; Located in Brentwood</p>
    </div>
  </article>
  <article class="review" style="left:18px;top:152px;width:473px;height:85px">
    <div class="source"><span class="source-name"><i></i>Searchly</span></div>
    <div class="review-body">
      <h3 class="review-title">Positive Professionalism, Quality &amp; Value</h3>
      <div class="scores"><span class="rel"><b>Reliability:</b> 9.38</span><span class="cou"><b>Courtesy:</b> 10</span><span class="tid"><b>Tidiness:</b> 9.84</span><span class="wor"><b>Workmanship:</b> 10</span></div>
      <p class="review-text">For the city, the spring trade fair is what the summer games were to the coast, just that the travel situation is not a concern in the region. The event which has been delayed by a year due to the weather, is seeing locals complain about the long wait for cabs but is also seen to be a major boost for tourism and a boost for the economy.</p>
      <p class="verified" style="margin-top:6px">Verified 28th September 2021 &nbsp;|&nbsp; Located in Brentwood</p>
    </div>
  </article>
  <article class="review" style="left:18px;top:247px;width:473px;height:85px">
    <div class="source"><span class="source-name"><i></i>Hollr</span></div>
    <div class="review-body">
      <h3 class="review-title">Brilliant all round professional, friendly service</h3>
      <div class="scores"><span class="rel"><b>Reliability:</b> 9.38</span><span class="cou"><b>Courtesy:</b> 10</span><span class="tid"><b>Tidiness:</b> 9.84</span><span class="wor"><b>Workmanship:</b> 10</span></div>
      <p class="review-text">For the city, the spring trade fair is what the summer games were to the coast, just that the travel situation is not a concern in the region. The event which has been delayed by a year due to the weather, is seeing locals complain about the long wait for cabs but is also seen to be a major boost for tourism and a boost for the economy.</p>
      <p class="verified" style="margin-top:6px">Verified 28th September 2021 &nbsp;|&nbsp; Located in Brentwood</p>
    </div>
  </article>
  <article class="review" style="left:18px;top:342px;width:473px;height:85px">
    <div class="source"><span class="source-name"><i></i>Vouchly</span></div>
    <div class="review-body">
      <h3 class="review-title">Best all round professional service</h3>
      <div class="scores"><span class="rel"><b>Reliability:</b> 9.38</span><span class="cou"><b>Courtesy:</b> 10</span><span class="tid"><b>Tidiness:</b> 9.84</span><span class="wor"><b>Workmanship:</b> 10</span></div>
      <p class="review-text">For the city, the spring trade fair is what the summer games were to the coast, just that the travel situation is not a concern in the region. The event which has been delayed by a year due to the weather, is seeing locals complain about the long wait for cabs but is also seen to be a major boost for tourism and a boost for the economy.</p>
      <p class="verified" style="margin-top:6px">Verified 28th September 2021 &nbsp;|&nbsp; Located in Brentwood</p>
    </div>
  </article>

  <div class="load-more" style="left:195px;top:460px">Load More</div>
  <div class="powered" style="left:403px;top:458px"><span class="powered-mark"></span><div class="powered-text"><small>Powered by</small><strong>ReviewHive</strong></div></div>
</section>

<!-- ============ MOBILE ============ -->
<div class="size-label" style="left:880px;top:24px">428</div>
<section class="widget widget-mobile" style="left:880px;top:59px;width:170px;height:912px">
  <div class="header">
    <div class="rating-stars">
      <svg><use href="#star-badge"/></svg><svg><use href="#star-badge"/></svg><svg><use href="#star-badge"/></svg><svg><use href="#star-badge"/></svg><svg><use href="#star-badge"/></svg>
    </div>
    <p class="score-text">Combined Review Score of: 4.3 out of 5</p>
  </div>
  <div class="filter" style="left:28px;top:53px">Filter Results<svg><use href="#chevron"/></svg></div>

  <article class="review is-active" style="top:83px">
    <div class="source"><span class="source-name"><i></i>Fixmark</span></div>
    <div class="review-body">
      <h3 class="review-title">Front door with windows each side and side windows</h3>
      <div class="scores"><span class="rel"><b>Reliability:</b> 9.38</span><span class="tid"><b>Tidiness:</b> 9.84</span><span class="rel"><b>Courtesy:</b> 10</span><span class="tid"><b>Workmanship:</b> 10</span></div>
      <p class="review-text">For the city, the spring trade fair is what the summer games were to the coast, just that the travel situation is not a concern in the region. The event which has been delayed by a year due to the weather, is seeing locals complain about the long wait for cabs but is also seen to be a major boost for tourism and a boost for the economy.</p>
      <p class="verified">Verified 28th September 2021<br>Located in Brentwood</p>
    </div>
  </article>
  <article class="review" style="top:268px">
    <div class="source"><span class="source-name"><i></i>Searchly</span></div>
    <div class="review-body">
      <h3 class="review-title">Front door with windows each side and side windows</h3>
      <div class="scores"><span class="rel"><b>Reliability:</b> 9.38</span><span class="tid"><b>Tidiness:</b> 9.84</span><span class="rel"><b>Courtesy:</b> 10</span><span class="tid"><b>Workmanship:</b> 10</span></div>
      <p class="review-text">For the city, the spring trade fair is what the summer games were to the coast, just that the travel situation is not a concern in the region. The event which has been delayed by a year due to the weather, is seeing locals complain about the long wait for cabs but is also seen to be a major boost for tourism and a boost for the economy.</p>
      <p class="verified">Verified 28th September 2021<br>Located in Brentwood</p>
    </div>
  </article>
  <article class="review" style="top:454px">
    <div class="source"><span class="source-name"><i></i>Hollr</span></div>
    <div class="review-body">
      <h3 class="review-title">Front door with windows each side and side windows</h3>
      <div class="scores"><span class="rel"><b>Reliability:</b> 9.38</span><span class="tid"><b>Tidiness:</b> 9.84</span><span class="rel"><b>Courtesy:</b> 10</span><span class="tid"><b>Workmanship:</b> 10</span></div>
      <p class="review-text">For the city, the spring trade fair is what the summer games were to the coast, just that the travel situation is not a concern in the region. The event which has been delayed by a year due to the weather, is seeing locals complain about the long wait for cabs but is also seen to be a major boost for tourism and a boost for the economy.</p>
      <p class="verified">Verified 28th September 2021<br>Located in Brentwood</p>
    </div>
  </article>
  <article class="review" style="top:639px">
    <div class="source"><span class="source-name"><i></i>Vouchly</span></div>
    <div class="review-body">
      <h3 class="review-title">Front door with windows each side and side windows</h3>
      <div class="scores"><span class="rel"><b>Reliability:</b> 9.38</span><span class="tid"><b>Tidiness:</b> 9.84</span><span class="rel"><b>Courtesy:</b> 10</span><span class="tid"><b>Workmanship:</b> 10</span></div>
      <p class="review-text">For the city, the spring trade fair is what the summer games were to the coast, just that the travel situation is not a concern in the region. The event which has been delayed by a year due to the weather, is seeing locals complain about the long wait for cabs but is also seen to be a major boost for tourism and a boost for the economy.</p>
      <p class="verified">Verified 28th September 2021<br>Located in Brentwood</p>
    </div>
  </article>

  <div class="load-more" style="left:26px;top:828px">Load More</div>
  <div class="powered" style="left:43px;top:868px"><span class="powered-mark"></span><div class="powered-text"><small>Powered by</small><strong>ReviewHive</strong></div></div>
</section>

</body>
</html>
```